Business Card Design

We have a group of different function companies owned and operated by one person. We are located in the Dallas Fort Worth area in Texas. We develop properties to where we are owners and develop properties that are not ours as well. We build custom homes and commercial buildings. We also do residential and commercial remodeling. We also own commercial properties in which we lease office space. We are trying to merge all we do into one card and have done so already into one website. We initially had thought of having a logo made with HV in nice attractive lettering maybe as a watermark. We are open to the color scheme but no neons or pastels.

Project Deadline Extended
Reason: I am needing 2 different cards for two businesses.

Industry/Entity Type

Residential

Contact Information for Business Card

Harwell Ventures
4826 Mabry Ln. Suite 417
Keller, Texas 76109
Land Development
Residential and Commercial Construction
Commercial Real Estate
Dale Wintermoot
www.harwellgrp.example
dale@harwellgrp.example
Cell: 817-555-0142
Office: 817-555-0187
Fax: 8175550163

```html
<!DOCTYPE html>
<html lang="en">
<head>
<meta charset="utf-8">
<title>Harwell Ventures – Business Card</title>
<link rel="stylesheet" href="https://fonts.googleapis.com/css2?family=Merienda:wght@400;700&family=Signika:wght@600;700&family=Gelasio:wght@500&family=Ubuntu:wght@400&display=swap">
<style>
  :root {
    --bg: #2a2a2a;
    --card: #ffffff;
    --orange: #e8582a;
    --red: #d63a2a;
    --charcoal: #2f2f2f;
    --grey: #505050;
    --green: #4cae3c;
    --ink: #1e1e1e;
  }
  * { margin: 0; padding: 0; box-sizing: border-box; }
  html, body { width: 1200px; height: 601px; overflow: hidden; }
  body { background: var(--bg); position: relative; }

  .card {
    position: absolute;
    width: 550px;
    height: 314px;
    background: var(--card);
    overflow: hidden;
    top: 144px;
  }
  .card--contact { left: 35px; }
  .card--brand { left: 615px; }

  .brand-mark { position: absolute; background: var(--orange); }
  .brand-name {
    position: absolute;
    font-family: "Merienda", cursive;
    font-weight: 700;
    color: var(--grey);
    white-space: nowrap;
  }

  .card--contact .brand-mark { left: 70px; top: 62px; width: 72px; height: 72px; }
  .card--contact .brand-name { left: 22px; top: 150px; font-size: 19px; }

  .divider { position: absolute; left: 204px; top: 18px; }

  .phones {
    position: absolute;
    right: 28px;
    top: 18px;
    list-style: none;
    font-family: "Gelasio", serif;
    font-size: 16px;
    color: var(--ink);
  }
  .phones li { display: flex; align-items: center; gap: 8px; height: 30px; }
  .phones li.is-office { color: var(--orange); }
  .phones svg { width: 22px; height: 22px; display: block; }

  .person-name {
    position: absolute;
    left: 228px;
    top: 118px;
    font-family: "Signika", sans-serif;
    font-weight: 700;
    font-size: 30px;
    color: var(--orange);
    white-space: nowrap;
  }
  .person-title {
    position: absolute;
    left: 300px;
    top: 156px;
    font-family: "Signika", sans-serif;
    font-weight: 700;
    font-size: 22px;
    color: var(--grey);
  }
  .website {
    position: absolute;
    right: 28px;
    top: 198px;
    font-family: "Merienda", cursive;
    font-weight: 700;
    font-size: 13px;
    color: var(--ink);
  }
  .address-bar {
    position: absolute;
    left: 212px;
    top: 222px;
    width: 338px;
    height: 34px;
    background: var(--charcoal);
    color: #fff;
    font-family: "Ubuntu", sans-serif;
    font-size: 12.5px;
    line-height: 34px;
    padding-left: 8px;
    white-space: nowrap;
  }
  .services-band {
    position: absolute;
    left: 0;
    bottom: 18px;
    width: 100%;
    height: 34px;
    background: var(--orange);
    font-family: "Merienda", cursive;
    font-size: 11.5px;
    line-height: 34px;
    color: var(--ink);
    text-align: center;
    white-space: nowrap;
  }

  .card--brand .brand-mark { left: 330px; top: 48px; width: 120px; height: 120px; }
  .card--brand .brand-name { left: 200px; top: 186px; font-size: 30px; }
  .card--brand .base-band {
    position: absolute; left: 0; bottom: 24px; width: 100%; height: 30px; background: var(--charcoal);
  }
  .card--brand .base-line {
    position: absolute; left: 0; bottom: 16px; width: 100%; height: 4px; background: var(--orange);
  }
</style>
</head>
<body>

<section class="card card--contact">
  <div class="brand-mark"></div>
  <div class="brand-name">Harwell Ventures</div>

  <svg class="divider" width="4" height="220" viewBox="0 0 4 220">
    <line x1="2" y1="0" x2="2" y2="220" stroke="#d63a2a" stroke-width="2" stroke-dasharray="18 10"/>
  </svg>

  <ul class="phones">
    <li>
      <svg viewBox="0 0 22 22"><rect width="22" height="22" rx="4" fill="#4cae3c"/><path d="M7 5l2.5 0 1 3-1.5 1.2a8 8 0 0 0 3.8 3.8L14 11.5l3 1v2.5c0 .8-.7 1.3-1.5 1.2A10.5 10.5 0 0 1 5.8 6.5C5.7 5.7 6.2 5 7 5z" fill="#fff"/></svg>
      <span>817-555-0142</span>
    </li>
    <li class="is-office">
      <svg viewBox="0 0 22 22"><rect width="22" height="22" rx="4" fill="#1e1e1e"/><path d="M4 9c0-2 3.5-3 7-3s7 1 7 3v1.5h-3.5V9h-7v1.5H4z" fill="#fff"/><rect x="6" y="11" width="10" height="6" rx="1" fill="#fff"/></svg>
      <span>817-555-0119</span>
    </li>
    <li>
      <svg viewBox="0 0 22 22"><rect width="22" height="22" rx="4" fill="#d63a2a"/><rect x="7" y="4" width="8" height="5" fill="#fff"/><rect x="4" y="9" width="14" height="6" rx="1" fill="#fff"/><rect x="7" y="13" width="8" height="5" fill="#fff" stroke="#d63a2a" stroke-width="1"/></svg>
      <span>817-555-0163</span>
    </li>
  </ul>

  <div class="person-name">Dale Wintermoot</div>
  <div class="person-title">President</div>
  <div class="website">www.harwellgrp.example</div>
  <div class="address-bar">4826 Mabry Ln. Suite 417 Keller, Texas 76109</div>
  <div class="services-band">·Land Development · Residential &amp; Commercial Construction · Commercial Real Estate</div>
</section>

<section class="card card--brand">
  <div class="brand-mark"></div>
  <div class="brand-name">Harwell Ventures</div>
  <div class="base-band"></div>
  <div class="base-line"></div>
</section>

</body>
</html>
```